Beer Bottle Label design for a range of beers

We require a label design for a beer bottle front bottle label, neck label and what would be nice the 26 mm crown cap bottle top for a small craft brewery.

We have called the brewery BrambleFox Brewing.

We set out with a simple goal - brew the beers we wanted to drink above all other brands. We are a small batch, brew shop, with a love for great beer made from superb malt, flavourful hops, local water, hand nurtured yeast and barrels of passion.

We are dedicated to creating small hand crafted batches of the best possible craft beer and we look forward to the day that great taste and extraordinarily good flavour defines the standard of great beer in the UK.

We would like to see line art style designs that incorporate (or change) the mascot picture attached - however if there is an artistic play on the BrambleFox theme we are totally open and will consider any interpretations that are attractive.

We would like the mascot on the bottle top which is a standard euro 26 mm crown cap. Three first attempts at a label looked good on paper but never transferred to looking striking on the bottle.

Ideally the label will be plain and contemporary as we would like to steer away from the classic-style teutonic and ornate heraldry style but we are open to suggestions.

The final design should take into account that we are artistic beer brewers.
Previous attempts at labels are visible on www.bramblefox-example.co.uk

Target Market(s)

Restaurants, Bars, Small events

Industry/Entity Type

Brewery

Requirements
Must have
• Label must fit a standard Beer Bottle.

Bottle Spec
Height: 222.4mm
Weight: 216g
Diameter: 61.2mm
Colours: Amber
Closure: 26mm Pry Crown

sample bottle data is available at http://www.vantrells-example.com/uploads/pdf/a52097c713e6c2a9ab3e9f3b1e8a6c9ead837390.pdf

Back of Label must include or leave space for legislated information: (However this can be addressed later as long as space is left on the back of the bottle)

The label must appear on a bottle in a single field of vision (i.e., can be viewed without having to turn the bottle), except for the back label with brewer’s details, the Lot number, ABV and allergenic ingredients, etc.
Nice to have
• Fresh Logo Idea for Bramblefox Brewing that is incorporated across beer range.
Should not have
• Should not attract attention of children. Pendrick Mill brewery in the UK have recently had their label banned as it is overly child 'friendly'.

```html
<!DOCTYPE html>
<html lang="en">
<head>
<meta charset="utf-8">
<title>BrambleFox Brewing – Ashcombe Amber label</title>
<link rel="stylesheet" href="https://fonts.googleapis.com/css2?family=Josefin+Sans:wght@300;400;700&family=Questrial&display=swap">
<style>
  :root {
    --paper: #ffffff;
    --label-white: #fbf8f4;
    --ale-orange: #e8922f;
    --band-orange: #e9a055;
    --mascot-brown: #7a3f2e;
    --ink-brown: #6b3a2c;
    --soft-grey: #e9e4de;
  }
  * { box-sizing: border-box; margin: 0; padding: 0; }
  html, body {
    width: 1200px;
    height: 1000px;
    overflow: hidden;
    background: var(--paper);
  }
  .label-sheet {
    position: relative;
    width: 1200px;
    height: 1000px;
    display: flex;
    flex-direction: column;
    align-items: center;
    justify-content: center;
    gap: 90px;
  }

  /* Round front label */
  .roundel {
    position: relative;
    width: 440px;
    height: 440px;
    border-radius: 50%;
    background: var(--label-white);
    box-shadow: 0 0 0 1px var(--soft-grey);
  }
  .roundel__ring {
    position: absolute;
    inset: 22px;
  }
  .roundel__content {
    position: absolute;
    inset: 0;
    display: flex;
    flex-direction: column;
    align-items: center;
    justify-content: center;
    gap: 14px;
  }
  .roundel__mascot {
    width: 230px;
    height: 120px;
    border-radius: 120px 120px 30px 60px;
    background: linear-gradient(180deg, var(--mascot-brown) 0%, #8d4c37 70%, var(--label-white) 71%);
    margin-top: -20px;
  }
  .brand-name {
    font-family: "Questrial", sans-serif;
    font-weight: 400;
    font-size: 40px;
    line-height: 1.05;
    color: var(--ink-brown);
    text-align: center;
    letter-spacing: 0.5px;
  }

  /* Wrap band label */
  .band {
    width: 1000px;
    background: var(--label-white);
    box-shadow: 0 0 0 1px var(--soft-grey);
    font-family: "Josefin Sans", sans-serif;
  }
  .band__tagline {
    height: 58px;
    display: flex;
    align-items: center;
    justify-content: center;
    color: var(--ale-orange);
    font-weight: 700;
    font-size: 20px;
    letter-spacing: 5px;
    text-transform: uppercase;
  }
  .band__title-row {
    height: 96px;
    background: var(--band-orange);
    display: flex;
    align-items: center;
    justify-content: space-between;
    padding: 0 48px;
    color: var(--label-white);
  }
  .band__volume,
  .band__abv {
    font-size: 20px;
    font-weight: 400;
    letter-spacing: 2px;
    width: 140px;
  }
  .band__abv { text-align: right; }
  .band__beer-name {
    font-weight: 300;
    font-size: 50px;
    letter-spacing: 9px;
    text-transform: uppercase;
    padding-top: 6px;
  }
  .band__origin {
    height: 62px;
    display: flex;
    align-items: center;
    justify-content: center;
    gap: 10px;
    color: var(--ink-brown);
    font-size: 20px;
    letter-spacing: 2.5px;
    text-transform: uppercase;
  }
  .band__origin strong { font-weight: 700; }
  .band__origin span { font-weight: 400; }
  .band__rule {
    height: 3px;
    background: var(--soft-grey);
  }
</style>
</head>
<body>
  <main class="label-sheet">
    <section class="roundel">
      <svg class="roundel__ring" viewBox="0 0 396 396" aria-hidden="true">
        <circle cx="198" cy="198" r="186" fill="none" stroke="var(--ale-orange)" stroke-width="5"/>
        <circle cx="198" cy="198" r="166" fill="none" stroke="var(--ale-orange)" stroke-width="26" opacity="0.35"/>
        <circle cx="198" cy="198" r="150" fill="none" stroke="var(--ale-orange)" stroke-width="3"/>
      </svg>
      <div class="roundel__content">
        <div class="roundel__mascot" role="img" aria-label="Brewery mascot illustration"></div>
        <p class="brand-name">BrambleFox<br>Brewing</p>
      </div>
    </section>

    <section class="band">
      <p class="band__tagline">A supremely quaffable ale</p>
      <div class="band__title-row">
        <span class="band__volume">330ML</span>
        <h1 class="band__beer-name">Ashcombe Amber</h1>
        <span class="band__abv">3.5% ABV</span>
      </div>
      <div class="band__rule"></div>
      <p class="band__origin">
        <strong>Extraordinary beer</strong>
        <span>brewed in</span>
        <strong>Ashcombe, Surrey UK</strong>
      </p>
    </section>
  </main>
</body>
</html>
```